Dental website design - brightmolarhouse.net

We are looking to do a redesign for the website: brightmolarhouse.net

Please use Sections from this google Slide I created: https://slides.vantoreplan.net/deck/8kQwZr2LmNpT5vXyA7cB3dEf9GhJ0sUiVo/edit#page=id.p

Target Market(s)

Dentistry

Industry/Entity Type

Dental Clinic

Number of Pages Required

1 page

Colors
f68e4e
86cae7

Requirements
Must have
• Please use Sections from this google Slide I created: https://slides.vantoreplan.net/deck/8kQwZr2LmNpT5vXyA7cB3dEf9GhJ0sUiVo/edit#page=id.p

```html
<!DOCTYPE html>
<html lang="en">
<head>
<meta charset="utf-8">
<title>Bright Molar House – Dental Care for the Whole Family</title>
<link rel="stylesheet" href="https://fonts.googleapis.com/css2?family=Ubuntu:wght@500;700&family=Questrial&family=Montserrat:wght@400;500;600&family=Open+Sans:wght@400;600&display=swap">
<style>
:root{
  --accent:#f68e4e;
  --accent-deep:#e5783a;
  --sky:#86cae7;
  --sky-pale:#dcefF8;
  --ink:#1e1e1e;
  --charcoal:#262626;
  --white:#ffffff;
}
*{box-sizing:border-box;margin:0;padding:0}
html,body{width:1200px;height:4626px;overflow:hidden;background:var(--white)}
body{font-family:"Montserrat",sans-serif;color:var(--ink)}
.page{position:relative;width:1200px;height:4626px;overflow:hidden}
.abs{position:absolute}
h1,h2,h3{font-weight:400}

/* header */
.brand{left:172px;top:40px;display:flex;align-items:center;gap:12px}
.brand-dot{width:34px;height:34px;border-radius:50%;background:var(--sky)}
.brand-name{font-family:"Montserrat",sans-serif;font-weight:600;font-size:22px;color:var(--accent-deep);letter-spacing:.5px;line-height:1.1;width:200px}
.contact-chip{display:flex;align-items:center;gap:12px}
.chip-icon{width:64px;height:64px;border-radius:50%;border:3px solid var(--accent);border-left-color:var(--sky);display:flex;align-items:center;justify-content:center}
.chip-label{font-family:"Open Sans",sans-serif;font-size:12px;font-weight:600;color:var(--ink)}
.chip-value{font-family:"Open Sans",sans-serif;font-size:19px;font-weight:600;color:var(--accent-deep);line-height:1.25}

.nav{left:0;top:189px;width:1200px;height:68px;background:var(--accent)}
.nav ul{list-style:none;display:flex;position:absolute;left:172px;top:24px}
.nav li{font-family:"Open Sans",sans-serif;font-size:13px;font-weight:600;color:var(--white);text-transform:uppercase;margin-right:19px}

/* hero */
.hero-bg{left:0;top:257px;width:1200px;height:700px;background:linear-gradient(90deg,#e6f3f9 0%,#d2eaf5 60%,#bfe1f0 100%)}
.hero-photo{left:760px;top:335px;width:440px;height:500px;background:radial-gradient(ellipse at 50% 40%,#f1d3bf 0%,#d9ad93 42%,rgba(191,225,240,0) 75%)}
.hero-title{left:172px;top:398px;font-family:"Ubuntu",sans-serif;font-weight:500;font-size:56px;color:var(--ink)}
.hero-sub{left:172px;top:480px;font-family:"Open Sans",sans-serif;font-size:27px;color:var(--ink)}
.pill{display:inline-flex;align-items:center;justify-content:center;border-radius:31px;font-family:"Open Sans",sans-serif;text-transform:uppercase}
.btn-appointment{left:172px;top:560px;width:223px;height:62px;background:var(--accent);color:var(--white);font-size:16px}
.btn-phone{left:406px;top:560px;width:147px;height:62px;background:#2d2d2d;color:var(--white);font-size:16px}

.mission-title{left:0;top:945px;width:1200px;text-align:center;font-family:"Montserrat",sans-serif;font-weight:600;font-size:36px;color:var(--white)}
.mission-text{left:160px;top:1017px;width:880px;text-align:center;font-size:11.5px;line-height:28.5px;color:var(--white)}
.btn-mission{left:526px;top:1239px;width:147px;height:54px;background:var(--white);color:var(--accent-deep);font-family:"Montserrat",sans-serif;font-weight:600;font-size:17px}

/* why choose us */
.why-title{left:0;top:1508px;width:1200px;text-align:center;font-family:"Montserrat",sans-serif;font-weight:600;font-size:32px;color:#2b2b2b}
.why-sub{left:0;top:1568px;width:1200px;text-align:center;font-size:13px;line-height:25px;color:var(--ink)}
.card{width:417px;height:232px;background:var(--white);border-radius:30px;box-shadow:0 2px 14px rgba(0,0,0,.13)}
.card-icon{position:absolute;top:12px;width:147px;height:209px;border-radius:26px;display:flex;align-items:center;justify-content:center}
.card-icon.sky{background:var(--sky)}
.card-icon.accent{background:var(--accent)}
.card-body{position:absolute;top:30px;width:220px}
.card-title{font-family:"Questrial",sans-serif;font-size:23px;text-transform:uppercase;margin-bottom:12px;white-space:nowrap}
.card-text{font-size:11px;line-height:19px;text-align:justify;color:#333}
.card-more{position:absolute;bottom:33px;font-size:12.5px;font-weight:500;text-transform:uppercase}
.align-right{text-align:right}
.align-right .card-text{text-align-last:right}
.t-accent{color:var(--accent-deep)}
.t-ink{color:var(--ink)}

/* about */
.about-title{left:172px;top:2424px;width:420px;font-family:"Questrial",sans-serif;font-size:27px;line-height:37px;color:var(--white)}
.about-text{left:172px;top:2522px;width:412px;font-size:10.8px;line-height:27px;text-align:justify;color:var(--white)}
.about-call{left:172px;top:2718px;font-family:"Questrial",sans-serif;font-size:21px;color:var(--white)}
.about-link{left:172px;top:2751px;width:400px;font-size:13px;line-height:24px;color:var(--white);text-decoration:underline}

/* testimonials */
.video{left:106px;top:3037px;width:474px;height:320px;background:linear-gradient(135deg,#5fa9cc 0%,#86cae7 50%,#4d93b8 100%)}
.test-title{left:602px;top:3056px;width:420px;font-family:"Montserrat",sans-serif;font-weight:600;font-size:31px;line-height:38px;color:#2b2b2b}
.test-quote{left:602px;top:3141px;width:428px;font-style:italic;font-size:12.5px;line-height:25px;text-align:justify;color:var(--ink)}
.btn-test{left:602px;top:3285px;width:122px;height:47px;background:var(--accent);color:var(--white);font-family:"Montserrat",sans-serif;font-weight:500;font-size:14px}

/* gallery */
.gal-title{left:618px;top:3588px;font-family:"Questrial",sans-serif;font-size:27px;line-height:38px;color:var(--white)}
.gal-sub{left:620px;top:3686px;font-family:"Questrial",sans-serif;font-size:21px;color:var(--white)}
.gal-text{left:620px;top:3730px;width:410px;font-size:11.5px;line-height:24.8px;text-align:justify;color:var(--white)}
.btn-gal{left:620px;top:3912px;width:201px;height:54px;background:var(--white);color:var(--accent-deep);font-family:"Montserrat",sans-serif;font-weight:600;font-size:17px}

/* footer */
.foot-brand{left:172px;top:4222px;width:284px;height:227px;background:var(--white);display:flex;align-items:center;justify-content:center;gap:10px}
.foot-brand .brand-name{width:auto;font-size:20px}
.foot-nav{left:503px;top:4218px;list-style:none}
.foot-nav li{font-family:"Open Sans",sans-serif;font-size:13px;font-weight:600;color:var(--white);text-transform:uppercase;height:33px}
.foot-contact{left:711px;display:flex;align-items:center;gap:16px}
.foot-icon{width:60px;height:60px;border-radius:50%;border:3px solid var(--white);border-left-color:var(--sky);display:flex;align-items:center;justify-content:center}
.foot-label{font-family:"Open Sans",sans-serif;font-size:13px;color:var(--white)}
.foot-value{font-family:"Open Sans",sans-serif;font-size:17px;color:var(--white);line-height:1.35}
.foot-rule{left:172px;top:4526px;width:855px;height:1px;background:#8a8a8a}
.copyright{left:0;top:4563px;width:1200px;text-align:center;font-family:"Open Sans",sans-serif;font-size:12.5px;font-weight:600;color:var(--white)}
</style>
</head>
<body>
<div class="page">

  <svg width="0" height="0" style="position:absolute" aria-hidden="true">
    <defs>
      <path id="tooth" d="M20 14 C28 8 34 14 40 14 C46 14 52 8 60 14 C68 20 66 34 62 42 C58 52 58 70 52 70 C46 70 46 52 40 52 C34 52 34 70 28 70 C22 70 22 52 18 42 C14 34 12 20 20 14Z"/>
    </defs>
  </svg>

  <header>
    <div class="abs brand">
      <span class="brand-dot"></span>
      <span class="brand-name">BRIGHT MOLAR HOUSE</span>
    </div>

    <div class="abs contact-chip" style="left:503px;top:60px">
      <span class="chip-icon">
        <svg width="22" height="34" viewBox="0 0 22 34"><rect x="2" y="2" width="18" height="30" rx="3" fill="none" stroke="#2b2b2b" stroke-width="2.5"/><circle cx="11" cy="27" r="1.8" fill="#2b2b2b"/></svg>
      </span>
      <div>
        <div class="chip-label">PHONE:</div>
        <div class="chip-value">(555) 214-7730</div>
      </div>
    </div>

    <div class="abs contact-chip" style="left:727px;top:60px">
      <span class="chip-icon">
        <svg width="26" height="34" viewBox="0 0 26 34"><path d="M13 32 C6 22 3 17 3 12 A10 10 0 0 1 23 12 C23 17 20 22 13 32Z" fill="none" stroke="#2b2b2b" stroke-width="2.5"/><circle cx="13" cy="12" r="3.5" fill="none" stroke="#2b2b2b" stroke-width="2.5"/></svg>
      </span>
      <div>
        <div class="chip-label">ADDRESS:</div>
        <div class="chip-value">418 LINDEN PARK AVE #120<br>OAKMERE, OH 43990</div>
      </div>
    </div>
  </header>

  <nav class="abs nav">
    <ul>
      <li>Home</li>
      <li>About Us</li>
      <li>Patient Information</li>
      <li>Preventative Care</li>
      <li style="margin-right:25px">Dental Implants</li>
      <li>Restorative Dentistry</li>
      <li>Contact</li>
    </ul>
  </nav>

  <section class="hero">
    <div class="abs hero-bg"></div>
    <div class="abs hero-photo" role="img" aria-label="Photo of a smiling young woman touching her cheeks"></div>
    <h1 class="abs hero-title">BRIGHT MOLAR HOUSE</h1>
    <p class="abs hero-sub">Dental Care for the Whole Family</p>
    <span class="abs pill btn-appointment">Make an Appointment</span>
    <span class="abs pill btn-phone">(555) 214-7730</span>
  </section>

  <svg class="abs" style="left:0;top:0" width="1200" height="1422" viewBox="0 0 1200 1422" aria-hidden="true">
    <defs>
      <linearGradient id="missionBand" x1="0" y1="0" x2="1" y2="1">
        <stop offset="0" stop-color="#f89a5e"/>
        <stop offset=".5" stop-color="#f68e4e"/>
        <stop offset="1" stop-color="#ec7f3f"/>
      </linearGradient>
    </defs>
    <path d="M0,745 Q600,1020 1200,700 L1200,1422 L0,1422 Z" fill="url(#missionBand)"/>
    <path d="M0,735 Q600,1010 1200,690" fill="none" stroke="#ffffff" stroke-width="14"/>
  </svg>

  <section class="mission">
    <h2 class="abs mission-title">OUR MISSION</h2>
    <p class="abs mission-text">
      To be Committed to Dental Excellence in all our services that we provide to our patients.<br>
      To constantly strive to achieve the highest level of skills and modern techniques and equipment so we can provide our patients with the best that Dentistry has to offer.<br>
      Our vision is to be able to serve our patients and provide them with Modern Dentistry in a Comfortable Relaxed Environment.<br>
      We provide our patients with a Caring dental experience that helps them build a long-term relationship that is built on knowledge of their dental needs, trust, confidence, quality of work, and exceptional patient care.
    </p>
    <span class="abs pill btn-mission">READ MORE</span>
  </section>

  <section class="why">
    <h2 class="abs why-title">WHY CHOOSE US?</h2>
    <p class="abs why-sub">At Bright Molar House, we're a one stop shop for all your dental needs<br>You can count on a confident, exceptionally skilled and knowledgeable dentist to keep your smile healthy and beautiful</p>

    <article class="abs card" style="left:172px;top:1683px">
      <div class="card-body align-right" style="left:20px">
        <h3 class="card-title t-ink">Clear Aligners</h3>
        <p class="card-text">The invisible way to straighten your teeth without braces. To discuss clear braces in the Oakmere OH area, please feel free to contact us to schedule an appointment.</p>
      </div>
      <span class="card-more t-ink" style="right:175px">Read More</span>
      <div class="card-icon sky" style="right:12px">
        <svg width="96" height="96" viewBox="0 0 80 80" aria-hidden="true"><use href="#tooth" fill="none" stroke="#fff" stroke-width="3"/><path d="M14 30 Q40 44 66 30" fill="none" stroke="#fff" stroke-width="3"/></svg>
      </div>
    </article>

    <article class="abs card" style="left:611px;top:1683px">
      <div class="card-icon accent" style="left:12px">
        <svg width="96" height="96" viewBox="0 0 80 80" aria-hidden="true"><use href="#tooth" fill="none" stroke="#fff" stroke-width="3"/><path d="M10 4 V14 M5 9 H15" stroke="#fff" stroke-width="2.5"/><circle cx="70" cy="62" r="3" fill="#fff"/></svg>
      </div>
      <div class="card-body" style="left:177px">
        <h3 class="card-title t-accent">Teeth Whitening</h3>
        <p class="card-text">Having a beautiful smile may be even easier than you think. Many people achieve the look they've been dreaming of with our simple 'whitening' procedure.</p>
      </div>
      <span class="card-more t-accent" style="left:177px">Read More</span>
    </article>

    <article class="abs card" style="left:172px;top:1940px">
      <div class="card-body align-right" style="left:20px">
        <h3 class="card-title t-accent">Root Canal</h3>
        <p class="card-text">A root canal is one of the most common dental procedures performed, well over 14 million every year.</p>
      </div>
      <span class="card-more t-accent" style="right:175px">Read More</span>
      <div class="card-icon accent" style="right:12px">
        <svg width="96" height="96" viewBox="0 0 80 80" aria-hidden="true"><use href="#tooth" fill="none" stroke="#fff" stroke-width="3"/><path d="M32 26 Q30 44 28 62 M48 26 Q50 44 52 62" fill="none" stroke="#fff" stroke-width="2.5"/></svg>
      </div>
    </article>

    <article class="abs card" style="left:611px;top:1940px">
      <div class="card-icon sky" style="left:12px">
        <svg width="96" height="96" viewBox="0 0 80 80" aria-hidden="true"><use href="#tooth" fill="none" stroke="#fff" stroke-width="3" transform="translate(-6 4) scale(.9)"/><rect x="64" y="24" width="8" height="30" rx="2" fill="none" stroke="#fff" stroke-width="2.5"/><path d="M68 24 V14 M68 54 V64" stroke="#fff" stroke-width="2.5"/></svg>
      </div>
      <div class="card-body" style="left:177px">
        <h3 class="card-title t-ink">Sedation Dentistry</h3>
        <p class="card-text">We offer Sleep Dentistry for your comfort and care.</p>
      </div>
      <span class="card-more t-ink" style="left:177px">Read More</span>
    </article>
  </section>

  <svg class="abs" style="left:0;top:2280px" width="1200" height="660" viewBox="0 2280 1200 660" aria-hidden="true">
    <defs>
      <linearGradient id="familyPhoto" x1="0" y1="0" x2="1" y2="1">
        <stop offset="0" stop-color="#a9cf86"/>
        <stop offset=".5" stop-color="#e2c0a6"/>
        <stop offset="1" stop-color="#b9d9ea"/>
      </linearGradient>
    </defs>
    <path d="M0,2389 Q300,2340 598,2326 L598,2895 Q300,2880 0,2838 Z" fill="var(--accent)"/>
    <path d="M598,2286 L1200,2286 L1200,2790 Q900,2900 598,2933 Z" fill="url(#familyPhoto)"/>
  </svg>
  <div class="abs" style="left:640px;top:2330px;width:540px;height:500px" role="img" aria-label="Photo of a happy family: a boy, his mother and father smiling outdoors"></div>

  <section class="about">
    <h2 class="abs about-title">General Cosmetic and Implant Dentistry in Oakmere OH</h2>
    <p class="abs about-text">The Bright Molar House-General Cosmetic and Implant Dentistry is a Dental Office in Oakmere Ohio. Bright Molar House was established in 1972 and has been a pioneer in providing Dental Implants and Advanced Dentistry in Oakmere, Fairbrook, Elm Ridge, Harlow and Surrounding area. Our Dentists believe in making a difference in our patient's lives by providing a dental experience that is different in a happy and positive way.</p>
    <p class="abs about-call">A new smile is just a phone call away!</p>
    <p class="abs about-link">Call us now to schedule a free consultation at Bright Molar House Phone Number(555) 214-7730.</p>
  </section>

  <section class="testimonials">
    <div class="abs video" role="img" aria-label="Video still of a patient speaking about his experience"></div>
    <svg class="abs" style="left:306px;top:3164px" width="70" height="70" viewBox="0 0 70 70" aria-hidden="true">
      <circle cx="35" cy="35" r="32" fill="rgba(255,255,255,.25)" stroke="#ffffff" stroke-width="3"/>
      <path d="M27 21 L50 35 L27 49 Z" fill="#ffffff"/>
    </svg>
    <h2 class="abs test-title">WHAT OUR PATIENTS ARE SAYING</h2>
    <p class="abs test-quote">Bright Molar House is one of the greatest dentist office I ever had the pleasure to be a patient of. The amount of professional experience they have is second to none. I highly recommend everyone to go there and let them give you the best dental care of their life.</p>
    <span class="abs pill btn-test">READ MORE</span>
  </section>

  <div class="abs" style="left:0;top:3800px;width:1200px;height:826px;background:var(--charcoal)"></div>
  <svg class="abs" style="left:0;top:3470px" width="1200" height="640" viewBox="0 3470 1200 640" aria-hidden="true">
    <defs>
      <linearGradient id="galleryPhoto" x1="0" y1="0" x2="1" y2="1">
        <stop offset="0" stop-color="#3a3a3a"/>
        <stop offset=".55" stop-color="#d8ad95"/>
        <stop offset="1" stop-color="#2e2e2e"/>
      </linearGradient>
    </defs>
    <path d="M0,3565 Q300,3480 598,3475 L598,4104 Q300,4090 0,4020 Z" fill="url(#galleryPhoto)"/>
    <path d="M598,3493 Q900,3500 1200,3565 L1200,3970 Q900,4050 598,4068 Z" fill="var(--accent)"/>
  </svg>
  <div class="abs" style="left:20px;top:3520px;width:560px;height:540px" role="img" aria-label="Photo of a smiling woman flossing her teeth"></div>

  <section class="gallery">
    <h2 class="abs gal-title">We Give<br>Special Attention to Detail</h2>
    <p class="abs gal-sub">View our client smile gallery</p>
    <p class="abs gal-text">Our philosophy is to provide our patients' knowledge of their dental needs, so they can choose and make an informed decision after a consult with our experienced dentists. We follow a "Patients First Philosophy" and use state of the art technology and techniques to ensure you leave our office with a smile.</p>
    <span class="abs pill btn-gal">SMILE MAKEOVERS</span>
  </section>

  <footer>
    <div class="abs foot-brand">
      <span class="brand-dot"></span>
      <span class="brand-name">BRIGHT MOLAR HOUSE</span>
    </div>

    <ul class="abs foot-nav">
      <li>Home</li>
      <li>About Us</li>
      <li>Patient Information</li>
      <li>Preventative Care</li>
      <li>Dental Implants</li>
      <li>Restorative Dentistry</li>
      <li>Contact</li>
    </ul>

    <div class="abs foot-contact" style="top:4216px">
      <span class="foot-icon">
        <svg width="20" height="32" viewBox="0 0 20 32"><rect x="2" y="2" width="16" height="28" rx="3" fill="none" stroke="#fff" stroke-width="2.5"/><circle cx="10" cy="25" r="1.7" fill="#fff"/></svg>
      </span>
      <div><div class="foot-label">PHONE:</div><div class="foot-value">(555) 214-7730</div></div>
    </div>

    <div class="abs foot-contact" style="top:4300px">
      <span class="foot-icon">
        <svg width="20" height="32" viewBox="0 0 20 32"><rect x="2" y="2" width="16" height="28" rx="3" fill="none" stroke="#fff" stroke-width="2.5"/><circle cx="10" cy="25" r="1.7" fill="#fff"/></svg>
      </span>
      <div><div class="foot-label">email:</div><div class="foot-value">info@brightmolarhouse.net</div></div>
    </div>

    <div class="abs foot-contact" style="top:4390px">
      <span class="foot-icon">
        <svg width="24" height="32" viewBox="0 0 24 32"><path d="M12 30 C5 21 3 16 3 11 A9 9 0 0 1 21 11 C21 16 19 21 12 30Z" fill="none" stroke="#fff" stroke-width="2.5"/><circle cx="12" cy="11" r="3.2" fill="none" stroke="#fff" stroke-width="2.5"/></svg>
      </span>
      <div><div class="foot-label">ADDRESS:</div><div class="foot-value">418 LINDEN PARK AVE #120<br>OAKMERE, OH 43990</div></div>
    </div>

    <div class="abs foot-rule"></div>
    <p class="abs copyright">COPYRIGHTS @ 2021 BRIGHT MOLAR HOUSE. ALL RIGHTS RESERVED.</p>
  </footer>

</div>
</body>
</html>
```